New Letterhead request for our Law Firm!

We are a small Estate Planning Firm who just got out logo redesigned. It's attached. We need some letterhead for our client welcome letters and so forth. Clean, bright, and approachable is our style. If you need the specifications for our color scheme or other versions of the logo file, we have those too. Visit our website to get an idea about our services/aesthetics:https://willowmere.law/

Target Market(s)

Adults 30-80

Colors

Designer to choose colors to be used in the design.

Requirements
Must have
• Logo with color. Contact information

```html
<!DOCTYPE html>
<html lang="en">
<head>
<meta charset="utf-8">
<title>Willowmere Law Firm – Letterhead</title>
<link rel="stylesheet" href="https://fonts.googleapis.com/css2?family=Open+Sans:wght@400;600&display=swap">
<style>
  :root {
    --paper: #ffffff;
    --ink: #4a4a4a;
    --ink-strong: #333333;
    --brand: #76a48a;
    --brand-dark: #5d9275;
    --watermark: #ececec;
  }
  * { margin: 0; padding: 0; box-sizing: border-box; }
  html, body { width: 1040px; height: 1200px; overflow: hidden; background: var(--paper); }
  body { font-family: "Open Sans", Arial, sans-serif; color: var(--ink); position: relative; }

  .letterhead { position: relative; width: 1040px; height: 1200px; }

  .brand { position: absolute; top: 30px; left: 0; width: 100%; display: flex; justify-content: center; align-items: center; gap: 10px; }
  .brand-dot { width: 46px; height: 46px; border: 3px solid var(--brand); border-radius: 50%; }
  .brand-name { font-weight: 600; font-size: 20px; line-height: 1.1; color: var(--brand); letter-spacing: 0.5px; }

  .watermark { position: absolute; left: 315px; top: 392px; width: 412px; height: 412px; border: 9px solid var(--watermark); border-radius: 50%; }

  .letter { position: absolute; left: 143px; top: 215px; width: 751px; font-size: 15px; line-height: 27px; }
  .issue-date { margin-bottom: 8px; }
  .recipient { line-height: 18px; margin-bottom: 50px; }
  .salutation { margin-bottom: 27px; }
  .letter-body p { text-align: justify; hyphens: auto; -webkit-hyphens: auto; margin-bottom: 27px; }
  .closing { margin-top: 53px; }
  .signatory { margin-top: 50px; }
  .signatory-name { font-size: 19px; font-weight: 600; color: var(--ink-strong); line-height: 26px; }
  .signatory-role { font-size: 15px; }

  .footer-curve { position: absolute; left: 0; top: 0; }
  .footer-contact { position: absolute; top: 1112px; width: 100%; text-align: center; font-size: 17px; color: var(--ink-strong); }
  .footer-contact .label { color: var(--brand-dark); font-weight: 600; }
  .footer-contact .accent { color: var(--brand-dark); }
  .footer-address { position: absolute; top: 1163px; width: 100%; text-align: center; font-size: 17px; color: #ffffff; }
</style>
</head>
<body>
<div class="letterhead">
  <header class="brand">
    <span class="brand-dot"></span>
    <span class="brand-name">WILLOWMERE<br>LAW FIRM</span>
  </header>

  <div class="watermark" aria-hidden="true"></div>

  <main class="letter">
    <p class="issue-date">Issuing Date: May 5, 2018</p>
    <p class="recipient">Name Of Employee Mr. XYZABC<br>Address of Employee<br>Address Line 2 etc..</p>
    <p class="salutation">Dear Mr.XYZABC</p>
    <div class="letter-body">
      <p>Lorem Ipsum has been the industry's standard dummy text ever since the 1500s, when an unknown printer took a galley of type and scrambled it to make a type specimen book. It has survived not only five centuries, but also the leap into electronic typesetting, remaining essentially unchanged. It was popularised in the 1960s with the release of Pressline sheets containing Lorem Ipsum passages, and more recently with desktop publishing software like Folio LayoutDesk including versions of Lorem Ipsum.</p>
      <p>Lorem Ipsum is simply dummy text of the printing and typesetting industry. Lorem Ipsum has been the industry's standard dummy text ever since the 1500s, when an unknown printer took a galley of type and scrambled it to make a type specimen book.</p>
      <p>It has survived not only five centuries, but also the leap into electronic typesetting, remaining essentially unchanged. It was popularised in the 1960s with the release of Pressline sheets containing Lorem IpsumIpsum passages.</p>
    </div>
    <p class="closing">Yours Sincerely</p>
    <div class="signatory">
      <p class="signatory-name">Daniel Harper</p>
      <p class="signatory-role">Managing Director</p>
    </div>
  </main>

  <svg class="footer-curve" width="1040" height="1200" viewBox="0 0 1040 1200" aria-hidden="true">
    <path d="M0 1118 Q520 1168 1040 1118" fill="none" stroke="var(--brand)" stroke-width="3"/>
    <path d="M0 1127 Q520 1180 1040 1127 L1040 1200 L0 1200 Z" fill="var(--brand)"/>
  </svg>

  <footer>
    <p class="footer-contact"><span class="label">P:</span> 555 014 2870 | www.<span class="accent">willowmere</span>.law</p>
    <p class="footer-address">1450 Lakeview Parkway, Suite 310 Maplewood, MN 55109</p>
  </footer>
</div>
</body>
</html>
```